Business Card Design

Consultation for design, construction athletic facilities specializing in synthetic turf systems and all weather running track systems.
Motto "True Owner Representation"
New Company that we'd like to highlight the LOGO first and foremost with the colors of the background and font as primary colors of the card too if possible. I've also attached a typical larger project design layout that could be used in the background to highlight our design and construction specialty.
Website is something we want very noticeable for driving traffic.
Target Market(s)
Athletic Directors, Designers, Government and Military, Contractors
Industry/Entity Type
Construction
Contact Information for Business Card
Peter L. Vandrell CFB, CTB
48317 W 63rd Ave
Harlow Ridge, WA 99482
C +1 503.555.0147
O +1 808.555.0182
Peter@fieldlaneco.example
www.fieldlaneco.example

```html
<!DOCTYPE html>
<html lang="en">
<head>
<meta charset="utf-8">
<title>Veldra Sport – Business Card</title>
<link href="https://fonts.googleapis.com/css2?family=Exo+2:wght@400;600&family=Open+Sans:wght@400;700&display=swap" rel="stylesheet">
<style>
  :root {
    --canvas: #e9e6e1;
    --card-black: #0b0b0c;
    --card-charcoal: #1d1d20;
    --accent-orange: #f0a52a;
    --accent-gold: #e6b25a;
    --text-white: #ffffff;
    --text-soft: #d9d9d9;
  }
  * { box-sizing: border-box; margin: 0; padding: 0; }
  html, body { width: 1200px; height: 1000px; overflow: hidden; }
  body {
    background: var(--canvas);
    font-family: "Open Sans", Arial, sans-serif;
    position: relative;
  }
  .card {
    position: absolute;
    left: 250px;
    width: 700px;
    height: 400px;
    background: linear-gradient(135deg, var(--card-charcoal) 0%, var(--card-black) 55%);
    overflow: hidden;
    box-shadow: 0 10px 30px rgba(0,0,0,0.25);
  }
  .card-contact { top: 60px; }
  .card-brand { top: 540px; }

  /* contact side */
  .field-layout-area {
    position: absolute;
    left: 150px; top: 84px; right: 0; bottom: 0;
    background: radial-gradient(ellipse closest-side at 45% 40%, rgba(90,90,95,0.35), rgba(20,20,22,0));
  }
  .web-band {
    position: absolute;
    left: 150px; top: 0; right: 0;
    height: 84px;
    background: var(--accent-orange);
    display: flex; align-items: center;
    padding-left: 36px;
  }
  .web-band .website {
    font-family: "Exo 2", Arial, sans-serif;
    font-size: 38px;
    color: var(--text-white);
    letter-spacing: 0.5px;
    white-space: nowrap;
  }
  .logo-small {
    position: absolute;
    left: 22px; top: 250px;
    display: flex; align-items: center; gap: 8px;
  }
  .logo-small .dot {
    width: 14px; height: 14px; border-radius: 50%;
    background: var(--accent-gold);
  }
  .logo-small .brand-name {
    font-family: "Exo 2", Arial, sans-serif;
    font-size: 13px; letter-spacing: 2px;
    color: var(--accent-gold);
    white-space: nowrap;
  }
  .corner-strip {
    position: absolute;
    left: 0; bottom: 22px;
    width: 96px; height: 18px;
    background: var(--accent-orange);
  }
  .person {
    position: absolute;
    left: 196px; top: 112px;
    width: 250px;
    color: var(--text-white);
    font-weight: 700;
    text-align: right;
    white-space: nowrap;
  }
  .person .name { font-size: 26px; line-height: 1.25; }
  .person .credential { font-size: 21px; margin-top: 4px; padding-right: 60px; }
  .address {
    position: absolute;
    right: 28px; top: 112px;
    width: 200px;
    text-align: right;
    color: var(--text-white);
    font-style: normal;
    font-size: 16px; line-height: 1.55;
    white-space: nowrap;
  }
  .contact-list {
    position: absolute;
    left: 220px; top: 270px;
    list-style: none;
    color: var(--text-soft);
    font-size: 17px; line-height: 1.7;
    white-space: nowrap;
  }
  .contact-list li { display: flex; align-items: center; gap: 12px; }
  .contact-list .icon {
    width: 22px; height: 22px; border-radius: 3px;
    background: var(--accent-orange);
    display: inline-flex; align-items: center; justify-content: center;
  }
  .contact-list .icon-blank { background: none; }

  /* brand side */
  .tagline {
    position: absolute;
    left: 34px; top: 26px;
    font-family: "Exo 2", Arial, sans-serif;
    font-weight: 600;
    font-size: 32px;
    color: var(--accent-orange);
    letter-spacing: 1.5px;
    white-space: nowrap;
  }
  .brand-glow {
    position: absolute;
    left: 120px; top: 60px;
    width: 460px; height: 260px;
    background: radial-gradient(ellipse closest-side at 50% 50%, rgba(240,165,42,0.32), rgba(240,165,42,0));
  }
  .logo-large {
    position: absolute;
    left: 0; right: 0; top: 190px;
    display: flex; justify-content: center; align-items: center; gap: 18px;
  }
  .logo-large .dot {
    width: 28px; height: 28px; border-radius: 50%;
    background: var(--accent-gold);
  }
  .logo-large .brand-name {
    font-family: "Exo 2", Arial, sans-serif;
    font-size: 58px;
    letter-spacing: 8px;
    color: var(--accent-gold);
    white-space: nowrap;
  }
</style>
</head>
<body>

<section class="card card-contact">
  <div class="field-layout-area" role="img" aria-label="Faint athletic field construction layout in the background"></div>
  <div class="web-band"><span class="website">www.fieldlaneco.example</span></div>
  <div class="logo-small"><span class="dot"></span><span class="brand-name">VELDRA SPORT</span></div>
  <div class="corner-strip"></div>

  <div class="person">
    <div class="name">Peter L. Vandrell</div>
    <div class="credential">CFB</div>
  </div>

  <address class="address">
    CTB<br>
    48317 W 63rd Ave<br>
    Harlow Ridge, WA 99482
  </address>

  <ul class="contact-list">
    <li><span class="icon">
      <svg width="14" height="14" viewBox="0 0 24 24"><path fill="#fff" d="M6.6 10.8a15 15 0 0 0 6.6 6.6l2.2-2.2a1 1 0 0 1 1-.25 11.4 11.4 0 0 0 3.6.57 1 1 0 0 1 1 1V20a1 1 0 0 1-1 1A17 17 0 0 1 3 4a1 1 0 0 1 1-1h3.5a1 1 0 0 1 1 1c0 1.250.2 2.45.57 3.57a1 1 0 0 1-.25 1z"/></svg>
    </span>C +1 503.555.0147</li>
    <li><span class="icon">
      <svg width="14" height="14" viewBox="0 0 24 24"><rect x="4" y="3" width="16" height="18" rx="2" fill="#fff"/><rect x="7" y="6" width="10" height="4" fill="#f0a52a"/></svg>
    </span>O +1 808.555.0182</li>
    <li><span class="icon icon-blank"></span>Peter@fieldlaneco.example</li>
  </ul>
</section>

<section class="card card-brand">
  <div class="tagline">True Owner Representation</div>
  <div class="brand-glow"></div>
  <div class="logo-large"><span class="dot"></span><span class="brand-name">VELDRA SPORT</span></div>
</section>

</body>
</html>
```